QRVoltana Wendlio Mobile Experience

Design the following Observation and Care Path mobile app pages so they are very modern, cool and engaging.
We would also like to modernize our current splash experience (attached).

Observation and Care Path wireframes:
https://k4mzq2.plorvex.com/#g=1&p=observations__-_categories

DO NOT SUBMIT LOGO REDESIGNS. Submit all screens for the above wireframes. If you can improve the Splash screen this is a bonus. Use the same color scheme and logo.

Competitive sample:
https://apps.trivelstore.com/store/apps/details?id=com.zorquin.iphone

```html
<!DOCTYPE html>
<html lang="en">
<head>
<meta charset="utf-8">
<title>Visit Detail – QRVoltana Wendlio</title>
<link rel="stylesheet" href="https://fonts.googleapis.com/css2?family=Montserrat:wght@400;500;600;700;800&display=swap">
<style>
  :root {
    --header-slate: #4b7589;
    --tab-orange: #f97b25;
    --tab-faded: #fbb58a;
    --action-blue: #2f62f6;
    --row-grey: #f4f4f4;
    --section-grey: #fafafa;
    --divider: #ececec;
    --task-number: #a9a9a9;
    --ink: #111111;
    --muted: #ababab;
    --alert-red: #f23b30;
    --help-amber: #f7a21b;
    --add-green: #4cd26b;
    --white: #ffffff;
  }
  * { box-sizing: border-box; margin: 0; padding: 0; }
  html, body { width: 675px; height: 1200px; overflow: hidden; background: var(--white); }
  body { font-family: "Montserrat", sans-serif; color: var(--ink); position: relative; }

  .status-bar { position: absolute; top: 0; left: 0; width: 675px; height: 36px; font-size: 18px; font-weight: 500; }
  .status-bar .carrier { position: absolute; left: 10px; top: 7px; display: flex; align-items: center; gap: 6px; }
  .status-bar .time { position: absolute; left: 0; right: 0; top: 7px; text-align: center; font-weight: 600; }
  .status-bar .battery { position: absolute; right: 12px; top: 7px; display: flex; align-items: center; gap: 6px; }

  .app-header { position: absolute; top: 36px; left: 0; width: 675px; height: 79px; background: var(--header-slate); color: var(--white); }
  .app-header .back { position: absolute; left: 28px; top: 30px; }
  .app-header .title { position: absolute; left: 0; right: 0; top: 24px; text-align: center; font-size: 25px; font-weight: 600; letter-spacing: 0.2px; }
  .header-icon { position: absolute; top: 27px; width: 27px; height: 27px; border-radius: 50%; color: var(--white); font-size: 16px; font-weight: 700; display: flex; align-items: center; justify-content: center; }
  .header-icon.help { left: 578px; background: var(--help-amber); }
  .header-icon.add { left: 626px; background: var(--add-green); font-size: 22px; font-weight: 500; }

  .tab-bar { position: absolute; top: 115px; left: 0; width: 675px; height: 87px; background: var(--tab-orange); }
  .tab { position: absolute; top: 31px; font-size: 24px; font-weight: 600; }
  .tab.active { left: 225px; width: 225px; text-align: center; color: var(--white); }
  .tab.inactive { left: 502px; color: var(--tab-faded); }
  .tab-indicator { position: absolute; left: 225px; top: 83px; width: 225px; height: 3px; background: var(--action-blue); border-radius: 2px; }

  .time-row { position: absolute; left: 0; width: 675px; height: 99px; background: var(--row-grey); }
  .time-row.clock-in { top: 202px; }
  .time-row.clock-out { top: 303px; }
  .time-row .stamp { position: absolute; left: 84px; top: 38px; font-size: 20px; font-weight: 600; }
  .pill-button { position: absolute; left: 504px; top: 23px; width: 146px; height: 54px; border-radius: 27px; background: var(--action-blue); color: var(--white); font-family: inherit; font-size: 20px; font-weight: 600; border: none; display: flex; align-items: center; justify-content: center; }

  .care-plan-header { position: absolute; top: 412px; left: 0; width: 675px; height: 71px; background: var(--section-grey); border-top: 1px solid var(--divider); border-bottom: 1px solid var(--divider); }
  .care-plan-header .label { position: absolute; left: 29px; top: 23px; font-size: 18px; font-weight: 600; }
  .care-plan-header .collapse { position: absolute; left: 626px; top: 22px; width: 27px; height: 27px; border-radius: 50%; background: var(--alert-red); }
  .care-plan-header .collapse::after { content: ""; position: absolute; left: 7px; top: 12.5px; width: 13px; height: 2px; background: var(--white); }

  .task-list { list-style: none; }
  .task { position: absolute; left: 0; width: 675px; height: 60px; }
  .task .number { position: absolute; left: 57px; top: 0; font-size: 47px; font-weight: 800; color: var(--task-number); line-height: 60px; }
  .task .name { position: absolute; left: 184px; top: 0; font-size: 24px; font-weight: 600; line-height: 60px; }
  .task-divider { position: absolute; left: 176px; width: 470px; height: 1px; background: var(--divider); }

  .observation-bar { position: absolute; top: 1102px; left: 29px; width: 617px; height: 98px; border-top: 1px solid var(--divider); }
  .observation-bar .placeholder { position: absolute; left: 55px; top: 38px; font-size: 20px; color: var(--muted); }
  .submit-button { position: absolute; left: 494px; top: 23px; width: 127px; height: 52px; border-radius: 26px; background: var(--muted); color: var(--white); border: none; font-family: inherit; font-size: 20px; font-weight: 700; display: flex; align-items: center; justify-content: center; }
</style>
</head>
<body>
  <div class="status-bar">
    <div class="carrier">
      <svg width="72" height="12" viewBox="0 0 72 12" aria-hidden="true">
        <circle cx="5" cy="6" r="5" fill="#000"/><circle cx="17" cy="6" r="5" fill="#000"/><circle cx="29" cy="6" r="5" fill="#000"/><circle cx="41" cy="6" r="5" fill="#000"/><circle cx="53" cy="6" r="5" fill="#000"/>
      </svg>
      <span>JL</span>
      <svg width="22" height="16" viewBox="0 0 22 16" aria-hidden="true">
        <path d="M11 15 L7.5 11.2 A5 5 0 0 1 14.5 11.2 Z" fill="#000"/>
        <path d="M4.6 8.3 A9 9 0 0 1 17.4 8.3" stroke="#000" stroke-width="2.4" fill="none"/>
        <path d="M1.5 5 A13.5 13.5 0 0 1 20.5 5" stroke="#000" stroke-width="2.4" fill="none"/>
      </svg>
    </div>
    <div class="time">9:41 AM</div>
    <div class="battery">
      <span>100%</span>
      <svg width="40" height="18" viewBox="0 0 40 18" aria-hidden="true">
        <rect x="1" y="1" width="34" height="16" rx="3" fill="none" stroke="#000" stroke-width="1.5"/>
        <rect x="3" y="3" width="30" height="12" rx="1.5" fill="#000"/>
        <rect x="36.5" y="6" width="2.5" height="6" rx="1" fill="#000"/>
      </svg>
    </div>
  </div>

  <header class="app-header">
    <svg class="back" width="18" height="16" viewBox="0 0 18 16" aria-label="Back">
      <path d="M17 8 H3 M8.5 2 L2.5 8 L8.5 14" stroke="#fff" stroke-width="2.6" fill="none" stroke-linecap="round" stroke-linejoin="round"/>
    </svg>
    <h1 class="title">Visit Detail Marcus Ellery</h1>
    <span class="header-icon help">?</span>
    <span class="header-icon add">+</span>
  </header>

  <nav class="tab-bar">
    <span class="tab active">Clock In/ Out</span>
    <span class="tab inactive">Directions</span>
    <span class="tab-indicator"></span>
  </nav>

  <section class="time-row clock-in">
    <span class="stamp">10/23 at 12:00</span>
    <button class="pill-button">Clock In</button>
  </section>
  <section class="time-row clock-out">
    <span class="stamp">10/23 at 16:00</span>
    <button class="pill-button">Clock Out</button>
  </section>

  <div class="care-plan-header">
    <span class="label">Plan of care tasks:</span>
    <span class="collapse"></span>
  </div>

  <ul class="task-list">
    <li class="task" style="top:510px"><span class="number">100</span><span class="name">Bathing</span></li>
    <li class="task-divider" style="top:596px"></li>
    <li class="task" style="top:625px"><span class="number">101</span><span class="name">Bathroom Assistance</span></li>
    <li class="task-divider" style="top:711px"></li>
    <li class="task" style="top:738px"><span class="number">102</span><span class="name">Grooming</span></li>
    <li class="task-divider" style="top:823px"></li>
    <li class="task" style="top:850px"><span class="number">103</span><span class="name">Cooking</span></li>
    <li class="task-divider" style="top:936px"></li>
    <li class="task" style="top:963px"><span class="number">104</span><span class="name">Cleaning</span></li>
  </ul>

  <footer class="observation-bar">
    <span class="placeholder">Check your observations</span>
    <button class="submit-button">Submit</button>
  </footer>
</body>
</html>
```